Vellmar Pools & Patio Homepage Design

I am looking for someone to design a one-page website for a company called Vellmar Pools & Patio. While the content will be different, the design should be similar to https://vellmarsite.com/pools-patio/.
Industry/Entity Type
Pool Cleaning Service
Number of Pages Required
1 page
Font styles to use
Other font styles liked:
- See brand guidelines

Requirements
Must have
- Must be similar in style https://vellmarsite.com/pools-patio/. Look at the Word Doc for the content.

```html
<!DOCTYPE html>
<html lang="en">
<head>
<meta charset="utf-8">
<title>Vellmar Pools &amp; Patio</title>
<link href="https://fonts.googleapis.com/css2?family=Montserrat:wght@700;800&family=Poppins:wght@400;500;600&display=swap" rel="stylesheet">
<style>
:root{
  --blue:#1b8bdb;
  --blue-deep:#0f6fc0;
  --green:#62c11a;
  --ink:#1e1e1e;
  --text:#333;
  --field:#e6e6e6;
  --dark:#15201f;
  --white:#fff;
}
*{box-sizing:border-box;margin:0;padding:0}
html,body{width:1200px;height:3805px;overflow:hidden;background:var(--white)}
body{position:relative;font-family:'Poppins',sans-serif;color:var(--text)}
.head{font-family:'Montserrat',sans-serif;font-weight:800;color:var(--ink)}
.btn{position:absolute;background:var(--green);color:var(--white);font-family:'Montserrat',sans-serif;font-weight:800;font-size:11px;display:flex;align-items:center;justify-content:center;letter-spacing:.3px}
.field{position:absolute;background:var(--field);font-size:11px;color:#555;padding:16px 0 0 22px}

.topbar{position:absolute;left:0;top:0;width:1200px;height:62px;background:var(--blue);display:flex;align-items:center;justify-content:center;gap:20px;color:var(--white);font-size:11px}
.topbar .ring{width:34px;height:34px;border-radius:50%;background:var(--white);display:flex;align-items:center;justify-content:center}
.topbar .sep{width:1px;height:16px;background:rgba(255,255,255,.6)}

.header{position:absolute;left:0;top:62px;width:1200px;height:108px;background:var(--white)}
.brand{position:absolute;display:flex;align-items:center;gap:10px;color:var(--green);font-weight:500;line-height:1}
.brand .mark{background:var(--green);border-radius:4px}
.nav{position:absolute;top:46px;font-size:12px;color:#333}
.icon-dot{position:absolute;top:42px;width:23px;height:23px;border-radius:50%;background:var(--blue)}

.hero{position:absolute;left:0;top:170px;width:1200px;height:622px;background:linear-gradient(100deg,#1a7fd0 0%,#2590dc 45%,#3a80a8 75%,#5a6a6a 100%)}
.hero h1{position:absolute;left:125px;top:160px;font-size:53px;line-height:63px;color:var(--white)}
.hero p{position:absolute;left:125px;top:378px;width:440px;font-size:15px;line-height:24px;font-weight:500;color:var(--white)}

.form-card{position:absolute;left:682px;top:347px;width:385px;height:520px;background:var(--white);box-shadow:0 8px 30px rgba(0,0,0,.15)}
.form-card h2{position:absolute;left:36px;top:45px;font-size:27px}
.form-card .rule{position:absolute;left:36px;top:94px;width:311px;height:1px;background:#7cc3ee}
.form-card .intro{position:absolute;left:36px;top:118px;width:300px;font-size:11px;line-height:18px}

.sec-title{position:absolute;left:0;width:1200px;text-align:center;font-size:44px}
.card-img{position:absolute;top:1065px;width:302px;height:197px}
.card-title{position:absolute;top:1300px;font-size:25px}
.card-text{position:absolute;top:1354px;width:300px;font-size:11px;line-height:18px}

.tech{position:absolute;left:0;top:1520px;width:1200px;height:622px;background:linear-gradient(90deg,#1d2a22,#15201f 60%,#1a2a2c)}
.tech-photo{position:absolute;left:125px;top:70px;width:465px;height:478px;background:linear-gradient(180deg,#ece9e1 0%,#d9cfc2 50%,#4a4e57 100%)}
.tech h2{position:absolute;left:638px;top:132px;font-size:44px;line-height:52px;color:var(--white)}
.tech p{position:absolute;left:638px;top:270px;width:420px;font-size:19px;line-height:29px;color:var(--white)}
.tech .name{position:absolute;left:638px;top:444px;font-size:27px;color:var(--green)}

.areas-sub{position:absolute;left:0;top:2310px;width:1200px;text-align:center;font-size:19px;line-height:30px;color:#333}
.map{position:absolute;left:0;top:2410px;width:1200px;height:287px;background:radial-gradient(ellipse 60% 90% at 50% 100%,#cfcfd3 0%,#e8e8ea 60%,#fff 100%)}

.contact{position:absolute;left:0;top:2697px;width:1200px;height:575px;background:var(--blue)}
.contact h2{position:absolute;left:125px;top:125px;font-size:44px;color:var(--white)}
.contact .lead{position:absolute;left:125px;top:202px;width:470px;font-size:14px;line-height:22.5px;color:var(--white)}
.contact .call{position:absolute;left:125px;top:345px;font-size:13px;color:var(--white)}
.contact .call b{font-size:24px;font-weight:500;margin-left:6px}
.contact-form{position:absolute;left:645px;top:100px;width:430px;height:375px;background:var(--white)}

.footer-col{position:absolute;top:3396px;font-size:22px;line-height:27px}
.flink{position:absolute;font-size:12px;color:#333}
.fcircle{position:absolute;width:36px;height:36px;border-radius:50%;background:var(--green);display:flex;align-items:center;justify-content:center}
.scircle{position:absolute;width:26px;height:26px;border-radius:50%;background:var(--blue)}
.bottombar{position:absolute;left:0;top:3745px;width:1200px;height:60px;background:var(--blue);color:var(--white);font-size:12px;font-weight:500;display:flex;align-items:center;justify-content:center}
</style>
</head>
<body>

<div class="topbar">
  <span class="ring"><svg width="16" height="16" viewBox="0 0 24 24"><path d="M6.6 10.8a15 15 0 006.6 6.6l2.2-2.2a1 1 0 011-.25 11.4 11.4 0 003.6.57 1 1 0 011 1V20a1 1 0 01-1 1A17 17 0 013 4a1 1 0 011-1h3.5a1 1 0 011 1c0 1.25.2 2.45.57 3.57a1 1 0 01-.25 1z" fill="#1b8bdb"/></svg></span>
  <span style="font-weight:500">972-555-0148</span>
  <span class="sep"></span>
  <span>Call Vellmar for a <b style="font-family:Montserrat,sans-serif;font-weight:800">FREE QUOTE</b></span>
</div>

<header class="header">
  <div class="brand" style="left:125px;top:33px;font-size:38px"><span class="mark" style="width:42px;height:42px"></span>vellmar</div>
  <span class="nav" style="left:417px">About</span>
  <span class="nav" style="left:493px">Services</span>
  <span class="nav" style="left:583px">Learn</span>
  <span class="nav" style="left:657px">Locations</span>
  <span class="nav" style="left:753px">FAQs</span>
  <span class="icon-dot" style="left:851px"></span>
  <span class="icon-dot" style="left:887px"></span>
  <div class="btn" style="left:933px;top:35px;width:142px;height:38px">GET A QUOTE</div>
</header>

<section class="hero" role="img" aria-label="Pool cleaning equipment and hose beside sparkling blue pool water">
  <h1 class="head">Keep Your Pool<br>Sparkling With<br>Vellmar!</h1>
  <p>We're Vellmar Pools &amp; Patio, and we specialize in pool cleaning and repair services that will keep your pool looking its best.</p>
</section>

<div class="form-card">
  <h2 class="head">Form</h2>
  <div class="rule"></div>
  <p class="intro">Lorem Ipsum is simply dummy text of the printing and typesetting industry.</p>
  <div class="field" style="left:36px;top:180px;width:312px;height:38px;padding-top:12px">Name</div>
  <div class="field" style="left:36px;top:231px;width:312px;height:39px;padding-top:12px">Email</div>
  <div class="field" style="left:36px;top:281px;width:312px;height:132px;padding-top:12px">Message</div>
  <div class="btn" style="left:36px;top:431px;width:140px;height:37px">SUBMIT</div>
</div>

<h2 class="sec-title head" style="top:958px">Our Services</h2>
<div class="card-img" style="left:125px;background:linear-gradient(135deg,#2a8fe0 0%,#2fa3ea 55%,#e8a14c 100%)" role="img" aria-label="Technician vacuuming a blue pool"></div>
<div class="card-img" style="left:448px;background:radial-gradient(circle at 50% 50%,#1f4fc4 0%,#27a9e6 45%,#5fd0f2 100%)" role="img" aria-label="Skimmer net with leaves over clear pool water"></div>
<div class="card-img" style="left:772px;background:linear-gradient(180deg,#d9e8f2 0%,#5b7b4a 40%,#2fb1e6 75%,#c9c9c9 100%)" role="img" aria-label="Backyard pool with garden and slide"></div>
<h3 class="card-title head" style="left:125px">Pool Cleaning</h3>
<h3 class="card-title head" style="left:448px">Pool Maintenance</h3>
<h3 class="card-title head" style="left:772px">Pool Repair</h3>
<p class="card-text" style="left:125px">Our weekly service includes chemical balancing, debris removal, wall and step scrubbing, and filter maintenance. Standard chemicals are included in the quoted price.</p>
<p class="card-text" style="left:448px">We perform regular checks on all your pool equipment to make sure it runs efficiently and safely.</p>
<p class="card-text" style="left:772px">From plumbing to equipment malfunctions, our qualified technicians can diagnose and repair any pool problem you may have.</p>

<section class="tech">
  <div class="tech-photo" role="img" aria-label="Portrait of the pool technician"></div>
  <h2 class="head">Meet Your<br>Technician</h2>
  <p>I understand that keeping your pool clean and well-maintained is a priority for you, which is why I'm committed to providing top-notch pool cleaning and repair services. Let's get started!</p>
  <div class="name head">Dale Harmon</div>
</section>

<h2 class="sec-title head" style="top:2228px">Our Services</h2>
<p class="areas-sub">Currently, we offer services in the Texas cities of Argyle,<br>Corinth, Flower Mound, and Lewisville.</p>
<div class="map" role="img" aria-label="Dotted world map with colourful location pins"></div>

<section class="contact">
  <h2 class="head">Contact Us</h2>
  <p class="lead">Contact us today at Vellmar Pools &amp; Patio, and let's discuss how our professionals can help bridge the gap between what your pool could be and what it actually is! Get ready to have a worry-free experience with quality service delivered right on time so you can start enjoying those waves anytime soon!</p>
  <p class="call">Give us a call today at <b>972-555-0193.</b></p>
  <div class="btn" style="left:125px;top:408px;width:148px;height:37px;font-size:10px">LEAD INTAKE FORM</div>
  <div class="contact-form">
    <div class="field" style="left:13px;top:13px;width:404px;height:49px">First Name</div>
    <div class="field" style="left:13px;top:75px;width:404px;height:49px">Last Name</div>
    <div class="field" style="left:13px;top:138px;width:404px;height:49px">Address</div>
    <div class="field" style="left:13px;top:200px;width:404px;height:49px">Phone</div>
    <div class="field" style="left:13px;top:263px;width:404px;height:49px">Email</div>
    <div class="btn" style="left:140px;top:325px;width:150px;height:38px">SUBMIT</div>
  </div>
</section>

<footer>
  <div class="brand" style="left:125px;top:3380px;font-size:42px"><span class="mark" style="width:48px;height:48px"></span>vellmar</div>
  <div class="fcircle" style="left:125px;top:3490px"><svg width="16" height="16" viewBox="0 0 24 24"><path d="M6.6 10.8a15 15 0 006.6 6.6l2.2-2.2a1 1 0 011-.25 11.4 11.4 0 003.6.57 1 1 0 011 1V20a1 1 0 01-1 1A17 17 0 013 4a1 1 0 011-1h3.5a1 1 0 011 1c0 1.25.2 2.45.57 3.57a1 1 0 01-.25 1z" fill="#fff"/></svg></div>
  <div class="fcircle" style="left:125px;top:3549px"><svg width="16" height="16" viewBox="0 0 24 24"><path d="M12 2a7 7 0 00-7 7c0 5 7 13 7 13s7-8 7-13a7 7 0 00-7-7zm0 9.5A2.5 2.5 0 1112 6.5a2.5 2.5 0 010 5z" fill="#fff"/></svg></div>
  <div class="fcircle" style="left:125px;top:3609px"><svg width="16" height="16" viewBox="0 0 24 24"><rect x="3" y="5" width="18" height="14" rx="2" fill="#fff"/><path d="M3 7l9 6 9-6" stroke="#62c11a" stroke-width="2" fill="none"/></svg></div>
  <span class="flink" style="left:183px;top:3499px">972-555-0148</span>
  <span class="flink" style="left:183px;top:3548px;line-height:20px">1180 Harbor Lane, Suite<br>410, Frisco, TX 75034</span>
  <span class="flink" style="left:183px;top:3619px">hello@vellmarsite.com</span>

  <h4 class="footer-col head" style="left:448px">Quick Links</h4>
  <span class="flink" style="left:448px;top:3505px">About</span>
  <span class="flink" style="left:448px;top:3533px">Services</span>
  <span class="flink" style="left:448px;top:3561px">Learn</span>
  <span class="flink" style="left:448px;top:3589px">Locations</span>
  <span class="flink" style="left:448px;top:3617px">FAQs</span>

  <h4 class="footer-col head" style="left:670px">RESOURCES</h4>
  <span class="flink" style="left:670px;top:3505px">How it Works</span>
  <span class="flink" style="left:670px;top:3533px">Privacy Policy</span>
  <span class="flink" style="left:670px;top:3561px">Promotions</span>
  <span class="flink" style="left:670px;top:3589px">Terms of Service</span>
  <span class="flink" style="left:670px;top:3617px">Sitemap</span>

  <h4 class="footer-col head" style="left:868px">CONNECT WITH<br>US ON SOCIAL</h4>
  <span class="scircle" style="left:868px;top:3501px"></span>
  <span class="scircle" style="left:868px;top:3539px"></span>
  <span class="scircle" style="left:868px;top:3576px"></span>
  <span class="scircle" style="left:868px;top:3614px"></span>
  <span class="flink" style="left:911px;top:3505px">Community/Vellmar</span>
  <span class="flink" style="left:911px;top:3543px">Updates/Vellmar</span>
  <span class="flink" style="left:911px;top:3580px">Videos/Vellmar</span>
  <span class="flink" style="left:911px;top:3618px">Gallery/Vellmar</span>
</footer>

<div class="bottombar">© 2023 Vellmarsite.com &nbsp;|&nbsp; All Rights Reserved</div>

</body>
</html>
```